Stationary Design for Norvack Digital

We are after a full stationary back business cards, letterheads, compliment slip, invoice template, delivery note and anything else we could use within the stationary pack.

We would also like an email footer creating.

Our company details to be included on all stationary:

Registered Name: Norvack Limited
Company Registration Number: 20483957
Website: www.norvackdigital.example
email: info@norvackdigital.example
Phone: 01632 960 417
Address: 48 Elmstead Lane Loughborough Leicestershire United Kingdom LE14 7QW

Industry/Entity Type

Business

```html
<!DOCTYPE html>
<html lang="en">
<head>
<meta charset="utf-8">
<title>Norvack Digital – Business Cards</title>
<link href="https://fonts.googleapis.com/css2?family=Source+Sans+3:wght@400;600&display=swap" rel="stylesheet">
<style>
  :root {
    --backdrop: #2e2927;
    --card: #121212;
    --card-edge: #1c1c1c;
    --ink: #f2f2f2;
    --muted: #cfcfcf;
    --accent: #2f62b0;
    --silver: #d4d4d4;
    --rule: #6a6a6a;
  }
  * { margin: 0; padding: 0; box-sizing: border-box; }
  html, body {
    width: 1200px; height: 814px; overflow: hidden;
    background: var(--backdrop);
    font-family: "Source Sans 3", "Myriad Pro", Arial, sans-serif;
  }
  .canvas {
    position: relative; width: 1200px; height: 814px;
  }
  .card {
    position: absolute; top: 253px;
    width: 540px; height: 308px;
    background: var(--card);
    border: 1px solid var(--card-edge);
    border-radius: 4px;
    box-shadow: 0 14px 30px rgba(0,0,0,.45);
    color: var(--ink);
  }
  .card--contact { left: 45px; }
  .card--brand { left: 615px; }

  /* Contact side */
  .wordmark {
    position: absolute; display: flex; align-items: center; gap: 10px;
    font-weight: 600; letter-spacing: .04em; white-space: nowrap;
  }
  .card--contact .wordmark {
    top: 52px; left: 142px;
    font-size: 30px; color: var(--accent);
  }
  .wordmark__dot {
    width: 12px; height: 12px; border-radius: 50%; background: currentColor;
  }
  .details {
    position: absolute; top: 145px; right: 270px;
    text-align: right; font-size: 15px; line-height: 23px;
  }
  .details__name { color: var(--accent); font-size: 20px; line-height: 26px; }
  .details__role { color: var(--muted); }
  .details__row { display: flex; justify-content: flex-end; align-items: center; gap: 7px; }
  .icon { width: 13px; height: 13px; flex: none; }
  .divider {
    position: absolute; left: 286px; top: 150px;
    width: 1px; height: 120px; background: var(--rule);
  }
  .address {
    position: absolute; top: 150px; left: 302px;
    font-size: 15px; line-height: 21px;
  }
  .address__company { font-weight: 600; }

  /* Brand side */
  .card--brand .wordmark {
    top: 112px; left: 0; width: 100%; justify-content: center;
    font-size: 48px; color: var(--silver); letter-spacing: .06em;
  }
  .card--brand .wordmark__dot { width: 16px; height: 16px; }
  .site {
    position: absolute; top: 206px; width: 100%; text-align: center;
    font-size: 13px; letter-spacing: .18em; color: var(--muted);
  }
</style>
</head>
<body>
<main class="canvas">
  <section class="card card--contact" aria-label="Business card, contact side">
    <div class="wordmark"><span class="wordmark__dot"></span>Norvack Digital</div>

    <div class="details">
      <div class="details__name">Elias Marlowe</div>
      <div class="details__role">CEO/Founder</div>
      <div class="details__row">01632 960 417
        <svg class="icon" viewBox="0 0 16 16" aria-hidden="true"><path fill="var(--accent)" d="M3.5 1.5l2.5 0 1 3.5-1.6 1.2a8 8 0 0 0 4.4 4.4L11 9l3.5 1v2.5c0 1-1 2-2 2A11 11 0 0 1 1.5 3.5c0-1 1-2 2-2z"/></svg>
      </div>
      <div class="details__row">info@norvackdigital.example
        <svg class="icon" viewBox="0 0 16 16" aria-hidden="true"><rect x="1" y="3" width="14" height="10" rx="1.5" fill="var(--accent)"/><path d="M1.5 4l6.5 5 6.5-5" stroke="var(--card)" stroke-width="1.3" fill="none"/></svg>
      </div>
      <div class="details__row">www.norvackdigital.example
        <svg class="icon" viewBox="0 0 16 16" aria-hidden="true"><circle cx="8" cy="8" r="7" fill="var(--accent)"/><path d="M1 8h14M8 1c-3 3.5-3 10.5 0 14M8 1c3 3.5 3 10.5 0 14" stroke="var(--card)" stroke-width="1" fill="none"/></svg>
      </div>
    </div>

    <div class="divider"></div>

    <address class="address" style="font-style:normal">
      <div class="address__company">Norvack Limited</div>
      <div>48 Elmstead Lane Loughborough</div>
      <div>Leicestershire</div>
      <div>United Kingdom LE14 7QW</div>
      <div>Reg. No: 20483957</div>
    </address>
  </section>

  <section class="card card--brand" aria-label="Business card, brand side">
    <div class="wordmark"><span class="wordmark__dot"></span>Norvack Digital</div>
    <div class="site">www.norvackdigital.example</div>
  </section>
</main>
</body>
</html>
```